Bright Meadow LLC business card

I help with the Marketing and Sales of various Natural, Organic, Eco Friendly and Healthy Main Stream products to Retail Corporate accounts as well as Independents and Distributors.I also highlight Private label items to these same Retail Corporate accounts.Cherish the Moments, Enjoy Life!

Speciality & Health Sales and Marketing

Target Market(s)

Men and Women

Industry/Entity Type

Business

Contact Information for Business Card

Bright Meadow, LLC
Janet Lou Brindall
418 West Fern Lane
Ste 3-274
Phoenix, AZ 85047
602-555-0173
jbrindall@veltramail.net

Requirements
Must have
• Nice, femine font
Something in the background or on a side with a softness
Nice to have
• Cherish the Moments, Enjoy Life
Should not have
• Hardness

```html
<!DOCTYPE html>
<html lang="en">
<head>
<meta charset="utf-8">
<title>Bright Meadow LLC – Business Card</title>
<link href="https://fonts.googleapis.com/css2?family=Lato:wght@300;400;700&display=swap" rel="stylesheet">
<style>
  :root {
    --page-bg: #ecebe8;
    --card-black: #111011;
    --card-black-soft: #201e20;
    --band-red: #e0232b;
    --band-red-soft: #e8464c;
    --text-white: #ffffff;
    --card-shadow: rgba(0, 0, 0, 0.22);
  }
  * { box-sizing: border-box; margin: 0; padding: 0; }
  html, body {
    width: 1200px;
    height: 900px;
    overflow: hidden;
    background: var(--page-bg);
    font-family: "Lato", Arial, sans-serif;
  }
  .canvas { position: relative; width: 1200px; height: 900px; }

  .card {
    position: absolute;
    width: 630px;
    height: 360px;
    background: radial-gradient(ellipse at 50% 40%, var(--card-black-soft), var(--card-black) 75%);
    border-radius: 10px;
    box-shadow: 0 16px 40px var(--card-shadow);
    overflow: hidden;
    color: var(--text-white);
  }

  /* Front */
  .card-front { left: 110px; top: 90px; }
  .card-front .brand {
    position: absolute;
    inset: 0;
    display: flex;
    flex-direction: column;
    align-items: center;
    justify-content: center;
    gap: 22px;
  }
  .brand-square {
    width: 70px; height: 58px;
    background: var(--text-white);
    border-radius: 12px;
  }
  .brand-name {
    font-weight: 300;
    font-size: 40px;
    letter-spacing: 1px;
    color: var(--text-white);
    white-space: nowrap;
  }

  /* Back */
  .card-back { left: 460px; top: 430px; }
  .back-header {
    position: absolute;
    left: 0; right: 0; top: 0; height: 138px;
    display: flex;
    align-items: center;
    padding-left: 70px;
    gap: 28px;
  }
  .back-header .brand-square { width: 78px; height: 64px; }
  .back-header .brand-name { font-size: 36px; }

  .contact-band {
    position: absolute;
    left: 0; right: 0; top: 138px; height: 180px;
    background: linear-gradient(100deg, var(--band-red), var(--band-red-soft));
    display: flex;
    justify-content: space-between;
    align-items: center;
    padding: 0 34px 0 48px;
  }
  .person { text-align: right; }
  .person-name { font-weight: 700; font-size: 24px; line-height: 1.15; }
  .person-title { font-weight: 400; font-size: 16px; line-height: 1.4; }
  .person-address { font-weight: 400; font-size: 17px; line-height: 1.3; margin-top: 8px; }

  .contact-list { list-style: none; }
  .contact-item {
    display: flex;
    align-items: center;
    gap: 9px;
    font-size: 16px;
    line-height: 1;
    height: 30px;
    white-space: nowrap;
  }
  .contact-icon { width: 18px; height: 18px; flex: none; }
</style>
</head>
<body>
<main class="canvas">

  <section class="card card-front" aria-label="Card front">
    <div class="brand">
      <div class="brand-square"></div>
      <div class="brand-name">Bright Meadow LLC</div>
    </div>
  </section>

  <section class="card card-back" aria-label="Card back">
    <header class="back-header">
      <div class="brand-square"></div>
      <div class="brand-name">Bright Meadow LLC</div>
    </header>

    <div class="contact-band">
      <div class="person">
        <p class="person-name">Janet Lou Brindall</p>
        <p class="person-title">Sales &amp; Marketing</p>
        <p class="person-address">418 West Fern Lane, Ste 3-274<br>Phoenix, AZ 85047</p>
      </div>

      <ul class="contact-list">
        <li class="contact-item">
          <svg class="contact-icon" viewBox="0 0 18 18"><rect width="18" height="18" rx="4" fill="#fff"/><path d="M5 4.5c.8-.5 1.6-.3 2 .5l.8 1.6c.3.6 0 1.2-.5 1.5 .6 1.3 1.4 2.1 2.6 2.6.3-.5.9-.8 1.5-.5l1.6.8c.8.4 1 1.2.5 2-.8 1.2-2.4 1.4-4 .5C7 12.2 5.6 10.7 4.6 8.6c-.8-1.6-.6-3.2.4-4.1z" fill="#e0232b"/></svg>
          <span>602-555-0173</span>
        </li>
        <li class="contact-item">
          <svg class="contact-icon" viewBox="0 0 18 18"><rect width="18" height="18" rx="4" fill="#fff"/><rect x="3.5" y="5" width="11" height="8" rx="1" fill="#e0232b"/><path d="M3.8 5.4 9 9.6l5.2-4.2" stroke="#fff" stroke-width="1.2" fill="none"/></svg>
          <span>jbrindall@veltramail.net</span>
        </li>
        <li class="contact-item">
          <svg class="contact-icon" viewBox="0 0 18 18"><rect width="18" height="18" rx="4" fill="#fff"/><path d="M7.5 10.5l3-3M8.2 5.8l1.2-1.2a2 2 0 0 1 2.9 2.9l-1.2 1.2M9.8 12.2l-1.2 1.2a2 2 0 0 1-2.9-2.9l1.2-1.2" stroke="#e0232b" stroke-width="1.6" stroke-linecap="round" fill="none"/></svg>
          <span>www.brightmeadow.net</span>
        </li>
      </ul>
    </div>
  </section>

</main>
</body>
</html>
```